Website Landing Page for Brightfall Systems

Create a custom designed website landing page for our business. Looking for a professional upscale design that incorporates our logo and logo colors into the theme. I want a standard fixed frame website, not a constant scrolling format that seems to be the trend. To start with I'm looking for more of the graphic design part, maybe a concept or theme, I don't expect to see a finished project. Not interested in generic templates or layouts.

The name of our company is Brightfall Systems and I've attached our logo below. I'd like to have the web page have the same look and feel of our logo, as well as the colors. Our company, Brightfall Systems does system design, installation, and programming, of residential and commercial Audio/Video and Automation systems. We do home theaters, lighting and building automation, video conferencing systems, security camera installations, conference rooms, projectors, distributed audio systems, and similar Technology projects. This will be a professional services/informational website. We will not sell products on this website. This website will be used to advertise our company and communicate our services to prospective customers. Having a well designed, professional and clean website is one way we want to distinguish our company from the competition.

Here are some examples of what I consider a professional well designed website
http://www.qorlamstudio.com/Work/

Last year we had our tradlo store designed (with PixelMarket) and I'm really happy with the way it turned out. You can see it at www.HolvenGearDepot.com I consider this to be a great design and looking for the same level of quality with this new website. However, do not copy or use any part of this design in this new project. This tradlo store is completely separate from our other company Brightfall Systems. I only mention this tradlo store an an example of good work.

Reason: Still going through designs.

Reason: Still working on project and have not had time to review all designs and request revisions.

Reason: Sill going through designs and requesting revisions

Reason: still going through all the submissions we received.

Target Market(s)

People interested in Audio/Video, home theaters, home automation. We do sales, system design, and programming. We typically work on larger projects with both residential and commercial customers.

Industry/Entity Type

Business

Number of Pages Required

1 page

Requirements
Must have
• Great design elements. Please use a white background. I think white goes well with our logo colors.

```html
<!DOCTYPE html>
<html lang="en">
<head>
<meta charset="utf-8">
<title>Brightfall Systems</title>
<link rel="stylesheet" href="https://fonts.googleapis.com/css2?family=Arimo:wght@400;700&display=swap">
<style>
:root{
  --blue:#3a7ec6;
  --blue-deep:#2d6fb8;
  --green:#3aa845;
  --green-deep:#2b9a3a;
  --ink:#3c3c3c;
  --muted:#555;
  --white:#fff;
  --footer:#434343;
  --footer-line:#5e5e5e;
}
*{margin:0;padding:0;box-sizing:border-box}
html,body{width:1200px;height:3636px;overflow:hidden;background:var(--white)}
body{position:relative;font-family:"Arimo",Arial,sans-serif;color:var(--ink)}
.abs{position:absolute}

/* header */
.site-header{left:0;top:0;width:1200px;height:54px;background:var(--white);z-index:5}
.brand{left:242px;top:10px;display:flex;align-items:center;gap:8px}
.brand-dot{width:30px;height:30px;border-radius:50%;border:3px solid var(--blue)}
.brand-name{font-size:12px;font-weight:700;color:var(--blue);line-height:13px;width:90px;text-transform:uppercase}
.main-nav{left:364px;top:22px;display:flex;gap:0}
.main-nav a{font-size:12px;color:var(--green-deep);text-decoration:none;width:68px}
.main-nav a.active{color:var(--green)}

/* hero */
.hero{left:0;top:54px;width:1200px;height:479px;
  background:linear-gradient(90deg,#2f6fb6 0%,#4f8fd0 22%,#6cb37a 50%,#3fae4f 72%,#2e9c3e 100%)}
.hero-ring{left:452px;top:205px;width:220px;height:220px;border:2px solid rgba(255,255,255,.8);border-radius:50%}
.hero-title{left:504px;top:282px;font-size:21px;color:var(--white)}
.hero-text{left:504px;top:312px;width:230px;font-size:11px;line-height:14px;color:var(--white)}
.hero-arrow{width:48px;height:48px;border-radius:50%;background:var(--white);display:flex;align-items:center;justify-content:center}

/* section titles */
.section-title{font-size:25px;color:var(--blue);font-weight:400}
.section-sub{font-size:11px;color:var(--green-deep)}
.body-copy{font-size:8.5px;line-height:11px;color:var(--muted)}
.body-copy p+p{margin-top:10px}

/* about */
.about-band{left:0;top:771px;width:1200px;height:296px;
  background:linear-gradient(90deg,#35a542 0%,#5fb567 40%,#4e8fcd 75%,#2f6fb6 100%)}
.about-photo{left:620px;top:614px;width:294px;height:294px;border-radius:50%;
  border:8px solid rgba(120,170,225,.75);
  background:radial-gradient(circle at 50% 40%,#9cc4e8 0%,#6e9a6a 55%,#4b7a3e 100%)}

/* services */
.deco-ring{border-radius:50%;border:22px solid rgba(58,126,198,.18)}
.card-back{background:var(--blue);border-radius:4px}
.card-photo{border-radius:4px}
.card-heading{font-size:13px;color:var(--green-deep)}
.card-copy{width:360px;font-size:9px;line-height:12px}
.card-copy p+p{margin-top:28px}

/* testimonial */
.quote-band{left:0;top:2654px;width:1200px;height:311px;
  background:linear-gradient(90deg,#3aa845 0%,#6db56d 35%,#7aa6cf 65%,#3a7ec6 100%)}
.quote-avatar{left:296px;top:2742px;width:136px;height:136px;border-radius:50%;border:6px solid #5d9ad6;
  background:linear-gradient(135deg,#a57a55,#6b4a33)}
.quote-title{left:427px;top:2771px;font-size:21px;color:var(--white)}
.quote-text{left:427px;top:2802px;width:475px;font-size:11px;line-height:14px;color:var(--white)}

/* closing */
.closing-band{left:0;top:3105px;width:1200px;height:90px;background:var(--blue)}
.closing-photo-strip{left:0;top:3195px;width:1200px;height:191px;
  background:linear-gradient(90deg,#7dbb7f 0%,#9cc6b4 45%,#8fb7df 100%)}
.closing-photo{left:245px;top:3011px;width:280px;height:280px;border-radius:50%;border:8px solid rgba(120,170,225,.8);
  background:radial-gradient(circle at 50% 45%,#e6d3a8 0%,#a98a62 60%,#6e5a40 100%)}
.closing-text{left:558px;top:3120px;width:540px;font-size:10px;line-height:13px;color:var(--white)}
.closing-text p+p{margin-top:10px}

/* footer */
.site-footer{left:0;top:3386px;width:1200px;height:250px;background:var(--footer);color:#e6e6e6}
.footer-brand{left:232px;top:3438px;width:270px;text-align:center}
.footer-brand-dot{width:78px;height:78px;border-radius:50%;border:4px solid var(--white);margin:0 auto 24px}
.footer-brand-name{font-size:17px;font-weight:700;letter-spacing:1px;color:var(--white);text-transform:uppercase;white-space:nowrap}
.footer-divider{width:1px;height:190px;background:var(--footer-line);top:3420px}
.footer-heading{font-size:12px;color:var(--white)}
.footer-list{list-style:none;font-size:9.5px;line-height:20px;color:#d8d8d8}
.social-item{display:flex;align-items:center;gap:8px}
.social-dot{width:9px;height:9px;border-radius:50%;background:#d8d8d8}
.newsletter{left:810px;top:3590px;width:128px;height:18px;border:1px solid #d0d0d0;background:var(--white);
  font-size:9px;color:#555;padding:3px 5px}
</style>
</head>
<body>

<header class="site-header abs">
  <div class="brand abs"><span class="brand-dot"></span><span class="brand-name">Brightfall Systems</span></div>
  <nav class="main-nav abs">
    <a class="active" href="#">Home</a><a href="#">Menu 1</a><a href="#">Menu 2</a><a href="#">Menu 3</a><a href="#">Menu 4</a><a href="#">Menu 5</a>
  </nav>
</header>

<section class="hero abs" role="img" aria-label="Glass office towers against a cloudy sky, tinted blue to green"></section>
<div class="hero-ring abs"></div>
<h1 class="hero-title abs">Lorem Ipsum</h1>
<p class="hero-text abs">Lorem Ipsum is simply dummy text of the printing and typesetting industry</p>
<div class="hero-arrow abs" style="left:546px;top:429px">
  <svg width="16" height="16" viewBox="0 0 16 16"><path d="M10 2 L4 8 L10 14" fill="none" stroke="#333" stroke-width="2"/></svg>
</div>
<div class="hero-arrow abs" style="left:604px;top:429px">
  <svg width="16" height="16" viewBox="0 0 16 16"><path d="M6 2 L12 8 L6 14" fill="none" stroke="#333" stroke-width="2"/></svg>
</div>

<section class="about">
  <h2 class="section-title abs" style="left:242px;top:575px">About</h2>
  <p class="section-sub abs" style="left:242px;top:606px">Lorem Ipsum is simply dummy text of the printing</p>
  <div class="body-copy abs" style="left:242px;top:636px;width:372px">
    <p>Lorem Ipsum is simply dummy text of the printing and typesetting industry. Lorem Ipsum has been the industry's standard dummy text ever since the 1500s, when an unknown printer took a galley of type and scrambled it to make a type specimen book. It has survived not only five centuries, but also the leap into electronic</p>
    <p>Lorem Ipsum is simply dummy text of the printing and typesetting industry. Lorem Ipsum has been the industry's standard dummy text ever since the 1500s, when an unknown printer took a galley of type and scrambled it to make a type specimen book. It has survived not only five centuries, but also the leap into electronic</p>
  </div>
  <div class="about-band abs" role="img" aria-label="City skyline panorama tinted green to blue"></div>
  <div class="about-photo abs" role="img" aria-label="Downtown towers behind a green park"></div>
</section>

<section class="services">
  <div class="deco-ring abs" style="left:-158px;top:1297px;width:340px;height:340px"></div>
  <div class="deco-ring abs" style="left:1038px;top:2172px;width:300px;height:300px"></div>

  <h2 class="section-title abs" style="left:242px;top:1150px">What we do</h2>
  <p class="section-sub abs" style="left:242px;top:1180px">Lorem Ipsum is simply dummy text of the printing</p>

  <!-- service 1 -->
  <div class="card-back abs" style="left:303px;top:1253px;width:206px;height:279px"></div>
  <div class="card-photo abs" role="img" aria-label="Tiered auditorium seating facing a projection screen" style="left:322px;top:1234px;width:204px;height:281px;background:linear-gradient(160deg,#c9c9c9,#6d6d6d 55%,#3a3f4a)"></div>
  <h3 class="card-heading abs" style="left:550px;top:1232px">Lorem Ipsum is simply dummy</h3>
  <div class="body-copy card-copy abs" style="left:550px;top:1262px">
    <p>Lorem Ipsum is simply dummy text of the printing and typesetting industry. Lorem Ipsum has been the industry's standard dummy text ever since the 1500s.Lorem Ipsum is simply dummy text of the printing and typesetting industry. Lorem Ipsum has been the industry's standard dummy text ever since the 1500s.</p>
    <p>Lorem Ipsum is simply dummy text of the printing and typesetting industry. Lorem Ipsum has been the industry's standard dummy text ever since the 1500s.Lorem Ipsum is simply dummy text of the printing and typesetting industry. Lorem Ipsum has been the industry's standard dummy text ever since the 1500s.</p>
    <p>Lorem Ipsum is simply dummy text of the printing and typesetting industry. Lorem Ipsum has been the industry's standard dummy text ever since the 1500s.Lorem Ipsum is simply dummy text of the printing and typesetting industry. Lorem Ipsum has been the industry's standard dummy text ever since the 1500s.</p>
    <p>Lorem Ipsum is simply dummy text of the printing and typesetting industry. Lorem Ipsum has been the industry's standard dummy text ever since the 1500s.Lorem</p>
  </div>

  <!-- service 2 -->
  <h3 class="card-heading abs" style="left:305px;top:1586px">Lorem Ipsum is simply dummy</h3>
  <div class="body-copy card-copy abs" style="left:305px;top:1616px">
    <p>Lorem Ipsum is simply dummy text of the printing and typesetting industry. Lorem Ipsum has been the industry's standard dummy text ever since the 1500s.Lorem Ipsum is simply dummy text of the printing and typesetting industry. Lorem Ipsum has been the industry's standard dummy text ever since the 1500s.</p>
    <p>Lorem Ipsum is simply dummy text of the printing and typesetting industry. Lorem Ipsum has been the industry's standard dummy text ever since the 1500s.Lorem Ipsum is simply dummy text of the printing and typesetting industry. Lorem Ipsum has been the industry's standard dummy text ever since the 1500s.</p>
    <p>Lorem Ipsum is simply dummy text of the printing and typesetting industry. Lorem Ipsum has been the industry's standard dummy text ever since the 1500s.Lorem Ipsum is simply dummy text of the printing and typesetting industry. Lorem Ipsum has been the industry's standard dummy text ever since the 1500s.</p>
    <p>Lorem Ipsum is simply dummy text of the printing and typesetting industry. Lorem Ipsum has been the industry's standard dummy text ever since the 1500s.Lorem</p>
  </div>
  <div class="card-back abs" style="left:703px;top:1605px;width:191px;height:264px"></div>
  <div class="card-photo abs" role="img" aria-label="Conference room with wall display and long table" style="left:679px;top:1585px;width:196px;height:252px;background:linear-gradient(180deg,#7a5a48 0%,#5b4236 50%,#c8ccd0 75%,#8d9298 100%)"></div>

  <!-- service 3 -->
  <div class="card-back abs" style="left:303px;top:1973px;width:206px;height:281px"></div>
  <div class="card-photo abs" role="img" aria-label="Bar counter with stools under pendant lights" style="left:322px;top:1954px;width:206px;height:281px;background:linear-gradient(180deg,#3b4a4a 0%,#25312f 45%,#8a5a32 75%,#2b2b2b 100%)"></div>
  <h3 class="card-heading abs" style="left:550px;top:1949px">Lorem Ipsum is simply dummy</h3>
  <div class="body-copy card-copy abs" style="left:550px;top:1979px">
    <p>Lorem Ipsum is simply dummy text of the printing and typesetting industry. Lorem Ipsum has been the industry's standard dummy text ever since the 1500s.Lorem Ipsum is simply dummy text of the printing and typesetting industry. Lorem Ipsum has been the industry's standard dummy text ever since the 1500s.</p>
    <p>Lorem Ipsum is simply dummy text of the printing and typesetting industry. Lorem Ipsum has been the industry's standard dummy text ever since the 1500s.Lorem Ipsum is simply dummy text of the printing and typesetting industry. Lorem Ipsum has been the industry's standard dummy text ever since the 1500s.</p>
    <p>Lorem Ipsum is simply dummy text of the printing and typesetting industry. Lorem Ipsum has been the industry's standard dummy text ever since the 1500s.Lorem Ipsum is simply dummy text of the printing and typesetting industry. Lorem Ipsum has been the industry's standard dummy text ever since the 1500s.</p>
    <p>Lorem Ipsum is simply dummy text of the printing and typesetting industry. Lorem Ipsum has been the industry's standard dummy text ever since the 1500s.Lorem</p>
  </div>

  <!-- service 4 -->
  <h3 class="card-heading abs" style="left:305px;top:2303px">Lorem Ipsum is simply dummy</h3>
  <div class="body-copy card-copy abs" style="left:305px;top:2333px">
    <p>Lorem Ipsum is simply dummy text of the printing and typesetting industry. Lorem Ipsum has been the industry's standard dummy text ever since the 1500s.Lorem Ipsum is simply dummy text of the printing and typesetting industry. Lorem Ipsum has been the industry's standard dummy text ever since the 1500s.</p>
    <p>Lorem Ipsum is simply dummy text of the printing and typesetting industry. Lorem Ipsum has been the industry's standard dummy text ever since the 1500s.Lorem Ipsum is simply dummy text of the printing and typesetting industry. Lorem Ipsum has been the industry's standard dummy text ever since the 1500s.</p>
    <p>Lorem Ipsum is simply dummy text of the printing and typesetting industry. Lorem Ipsum has been the industry's standard dummy text ever since the 1500s.Lorem Ipsum is simply dummy text of the printing and typesetting industry. Lorem Ipsum has been the industry's standard dummy text ever since the 1500s.</p>
    <p>Lorem Ipsum is simply dummy text of the printing and typesetting industry. Lorem Ipsum has been the industry's standard dummy text ever since the 1500s.Lorem</p>
  </div>
  <div class="card-back abs" style="left:667px;top:2327px;width:218px;height:286px"></div>
  <div class="card-photo abs" role="img" aria-label="Lounge bar seating beside tall windows" style="left:688px;top:2308px;width:206px;height:281px;background:linear-gradient(180deg,#9fb4c0 0%,#4e5a5c 45%,#9a6a3e 75%,#3a3a3a 100%)"></div>
</section>

<section class="testimonial">
  <div class="quote-band abs" role="img" aria-label="Bright living room interior tinted green to blue"></div>
  <svg class="abs" style="left:214px;top:2795px" width="20" height="26" viewBox="0 0 20 26"><path d="M15 2 L5 13 L15 24" fill="none" stroke="#fff" stroke-width="3"/></svg>
  <svg class="abs" style="left:966px;top:2795px" width="20" height="26" viewBox="0 0 20 26"><path d="M5 2 L15 13 L5 24" fill="none" stroke="#fff" stroke-width="3"/></svg>
  <div class="quote-avatar abs" role="img" aria-label="Wood-panelled home theater room"></div>
  <h3 class="quote-title abs">Lorem Ipsum</h3>
  <p class="quote-text abs">Lorem Ipsum is simply dummy text of the printing and typesetting industry. Lorem Ipsum has been the industry's standard dummy text ever since the 1500s.Lorem Ipsum is simply dummy text of the printing and typesetting industry. Lorem Ipsum has been the industry's standard dummy text ever since the 1500s.</p>
</section>

<section class="closing">
  <h2 class="section-title abs" style="left:558px;top:3033px">Lorem Ipsum</h2>
  <p class="section-sub abs" style="left:558px;top:3066px">Lorem Ipsum is simply dummy text of the printing</p>
  <div class="closing-band abs"></div>
  <div class="closing-photo-strip abs" role="img" aria-label="Living room with sofa and lamps, faded green to blue"></div>
  <div class="closing-photo abs" role="img" aria-label="Living room with a wall of screens and soft lighting"></div>
  <div class="closing-text abs">
    <p>Lorem Ipsum is simply dummy text of the printing and typesetting industry. Lorem Ipsum has been the industry's standard dummy text ever since the 1500s.</p>
    <p>Lorem Ipsum is simply dummy text of the printing and typesetting industry. Lorem Ipsum has been the industry's standard dummy text ever since the 1500s.</p>
  </div>
</section>

<footer class="site-footer abs"></footer>
<div class="footer-brand abs">
  <div class="footer-brand-dot"></div>
  <div class="footer-brand-name">Brightfall Systems</div>
</div>
<div class="footer-divider abs" style="left:507px"></div>
<div class="footer-divider abs" style="left:659px"></div>
<div class="footer-divider abs" style="left:781px"></div>

<div class="abs" style="left:550px;top:3448px">
  <h4 class="footer-heading">Menus</h4>
  <ul class="footer-list" style="margin-top:10px">
    <li>Home</li><li>Menu 1</li><li>Menu 2</li><li>Menu 3</li><li>Menu 4</li>
  </ul>
</div>
<div class="abs" style="left:691px;top:3448px">
  <h4 class="footer-heading">Follow us</h4>
  <ul class="footer-list" style="margin-top:10px">
    <li class="social-item"><span class="social-dot"></span>Friendlane</li>
    <li class="social-item"><span class="social-dot"></span>Chirpline</li>
    <li class="social-item"><span class="social-dot"></span>Snapgrid</li>
  </ul>
</div>
<div class="abs" style="left:810px;top:3448px;width:200px">
  <h4 class="footer-heading">Contact us</h4>
  <ul class="footer-list" style="margin-top:10px;line-height:13px">
    <li>hello@brightfallsystems.example</li>
    <li style="margin-top:7px">Harlow Court, Unit 14, 2nd floor<br>suite 8</li>
    <li style="margin-top:7px">SHOW MAP</li>
  </ul>
  <h4 class="footer-heading" style="margin-top:12px">Get in touch</h4>
  <p class="footer-list" style="line-height:14px;margin-top:4px">Subscribe to our newsletter</p>
</div>
<div class="newsletter abs">Your email</div>

</body>
</html>
```